依頼詳細
『Velva Prism ヴェルヴァプリズム』のアルミ袋デザインを依頼させて頂きます。

商品サイトがありますのでこのサイトにイメージを合わせて頂けたらと思います。
商品サイト  http://velvaprism-shop.net/item/

参考画像も貼っておきます。

色数は背景含めて3色でお願いします。
希望イメージは薄いピンクで背景はグラデーションをかけて下さい。
花や葉っぱなど、上品な感じの模様を背景に少し入れて下さい。(参考画像のような柄でお願いします)
記載項目
サブタイトル: 30歳を過ぎたらフルボディケア

商品名: Velva Prism  ヴェルヴァプリズム ← ローマ字の方を大きめに目立つように記載してほしいです。

プラセンタ、コラーゲン、ヒアルロン酸、プエラリア、ローヤルゼリー、
はと麦、真珠パウダーなどあらゆる美容成分をオールインワンにしました。←下の方にいれてほしい文章です。

1袋90粒入り
希望イメージ
シンプル 複雑
単色 カラフル
暗い 明るい
日常 高級
遊び心 厳粛
未来的 伝統的
女性的 男性的
希望する色
ピンク、白等で優しく綺麗な感じでお願いします。
納品ファイル
• イラストレーター形式 (.ai)
• フォトショップ形式 (.psd)
補足説明
依頼公開後の追記内容
■ 選んだ理由

ピンクと白を使った優しく上品な感じが、こちらのイメージとぴったり
あっていましたので選ばせて頂きました。

■ 提案者全員のお礼・コメント

たくさんの提案を本当にありがとうございました。
色んなタイプがあり、とても迷いました。
今回のイメージに合う提案もたくさんあり、本当に
ありがとうございました。

```html
<!DOCTYPE html>
<html lang="ja">
<head>
<meta charset="utf-8">
<title>Velva Prism パッケージ</title>
<link rel="stylesheet" href="https://fonts.googleapis.com/css2?family=Bodoni+Moda:wght@700&family=Noto+Serif+JP:wght@500;700&display=swap">
<style>
  :root {
    --magenta: #b3186d;
    --blush: #f2d5e4;
    --blush-deep: #e9bcd3;
    --white: #ffffff;
    --ink: #9c1560;
  }
  * { margin: 0; padding: 0; box-sizing: border-box; }
  html, body { width: 761px; height: 1200px; overflow: hidden; background: var(--white); }
  .canvas { position: relative; width: 761px; height: 1200px; font-family: "Noto Serif JP", serif; }

  .swatches { position: absolute; left: 20px; top: 22px; display: flex; gap: 16px; }
  .swatch { width: 46px; }
  .swatch-chip { width: 46px; height: 46px; border: 1px solid #999; }
  .swatch-label { font-family: Arial, sans-serif; font-size: 9px; color: #555; margin-top: 3px; }
  .chip-magenta { background: var(--magenta); }
  .chip-blush { background: var(--blush); }
  .chip-white { background: var(--white); }

  .pouch {
    position: absolute; left: 138px; top: 160px; width: 496px; height: 960px;
    border-radius: 14px; overflow: hidden;
    background: linear-gradient(180deg, #fbeef5 0%, #f7e2ed 40%, var(--blush) 100%);
    box-shadow: 0 0 0 1px #ecd3e0;
  }
  .pattern-top {
    position: absolute; right: 0; top: 0; width: 220px; height: 180px;
    background: radial-gradient(circle at 100% 0%, rgba(233,188,211,0.55), rgba(233,188,211,0) 70%);
  }
  .pattern-bottom {
    position: absolute; left: 0; bottom: 0; width: 100%; height: 430px;
    background: linear-gradient(180deg, rgba(233,188,211,0) 0%, rgba(233,188,211,0.55) 60%, rgba(226,170,199,0.7) 100%);
  }

  .tagline { position: absolute; left: 0; top: 112px; width: 496px; height: 104px; overflow: visible; }
  .tagline text { font-family: "Noto Serif JP", serif; font-weight: 500; font-size: 23px; fill: var(--magenta); letter-spacing: 1px; }

  .title-band { position: absolute; left: 0; top: 268px; width: 100%; height: 160px; background: var(--magenta); }
  .title-frame {
    position: absolute; left: 50px; top: 222px; width: 396px; height: 250px;
    background: var(--white); border-radius: 26px;
    box-shadow: 0 0 0 3px var(--white), 0 0 0 5px var(--magenta);
  }
  .frame-inner { position: absolute; inset: 10px; border: 1.5px solid var(--magenta); border-radius: 18px; }
  .product-name {
    position: absolute; left: 0; top: 18px; width: 100%; text-align: center;
    font-family: "Bodoni Moda", serif; font-weight: 700; color: var(--magenta);
    font-size: 64px; line-height: 66px;
  }
  .product-kana {
    position: absolute; left: 0; top: 172px; width: 100%; text-align: center;
    font-family: "Noto Serif JP", serif; font-weight: 700; color: var(--magenta);
    font-size: 22px; letter-spacing: 2px;
  }

  .ingredients {
    position: absolute; left: 0; top: 578px; width: 100%; text-align: center;
    font-size: 20px; line-height: 34px; color: var(--ink); font-weight: 500;
  }

  .dosage { position: absolute; left: 338px; top: 742px; width: 120px; text-align: center; color: var(--ink); }
  .dosage-daily { font-size: 14px; }
  .dosage-rule { height: 1px; background: var(--ink); margin: 4px 10px; }
  .dosage-count { font-size: 22px; font-weight: 700; }
  .capsule { position: absolute; left: 60px; top: -46px; }
</style>
</head>
<body>
<div class="canvas">
  <div class="swatches">
    <div class="swatch"><div class="swatch-chip chip-magenta"></div><div class="swatch-label">DIC-2628</div></div>
    <div class="swatch"><div class="swatch-chip chip-blush"></div><div class="swatch-label">DIC-3</div></div>
    <div class="swatch"><div class="swatch-chip chip-white"></div><div class="swatch-label">白</div></div>
  </div>

  <div class="pouch">
    <div class="pattern-top" role="img" aria-label="淡いピンクの花と葉の模様"></div>
    <div class="pattern-bottom" role="img" aria-label="淡いピンクの花と葉の模様"></div>

    <svg class="tagline" viewBox="0 0 496 104" aria-label="30歳を過ぎたらフルボディケア">
      <defs><path id="tagline-arc" d="M 36 98 Q 248 18 460 98"/></defs>
      <text text-anchor="middle"><textPath href="#tagline-arc" startOffset="50%">30歳を過ぎたらフルボディケア</textPath></text>
    </svg>

    <div class="title-band"></div>
    <div class="title-frame">
      <div class="frame-inner"></div>
      <h1 class="product-name">Velva<br>Prism</h1>
      <p class="product-kana">ヴェルヴァプリズム</p>
    </div>

    <p class="ingredients">
      プラセンタ、コラーゲン、ヒアルロン酸、<br>
      プエラリア、ローヤルゼリー、はと麦、<br>
      真珠パウダーなどあらゆる美容成分を<br>
      オールインワンにしました。
    </p>

    <div class="dosage">
      <svg class="capsule" width="60" height="44" viewBox="0 0 60 44" aria-hidden="true">
        <rect x="4" y="14" width="44" height="18" rx="9" fill="var(--magenta)" transform="rotate(-12 26 23)"/>
        <rect x="18" y="24" width="38" height="16" rx="8" fill="#d45a9a" transform="rotate(8 37 32)"/>
      </svg>
      <div class="dosage-daily">1日3粒</div>
      <div class="dosage-rule"></div>
      <div class="dosage-count">90粒入</div>
    </div>
  </div>
</div>
</body>
</html>
```